KA VERLINE

We need a letterhead design for an Image & Etiquette Consultancy company based in Singapore.

The services we provide are Personal Image Consultation, Image & Etiquette Workshop for schools and corporate.

The design should have our corporate colour as seen in the logo files I have uploaded.

Since our company helps clients with their image, the design should be aesthetically very appealing. It should reflect a very classy & elegant feel.

I will print the letterhead using my printer but most of the time will use it to write letters to my clients therefore the format should include MS Word.

```html
<!DOCTYPE html>
<html lang="en">
<head>
<meta charset="utf-8">
<title>KA VERLINE Letterhead</title>
<link href="https://fonts.googleapis.com/css2?family=Didact+Gothic&display=swap" rel="stylesheet">
<style>
  :root {
    --plum: #3d2549;
    --gold: #d9a514;
    --gold-light: #f0c52e;
    --gold-dark: #b8860b;
    --paper: #f2f2f2;
    --ink: #3a3a3a;
    --backdrop: #c9c5ca;
    --white: #ffffff;
  }
  html, body {
    margin: 0;
    padding: 0;
    width: 1200px;
    height: 1000px;
    overflow: hidden;
    background: var(--backdrop);
    font-family: "Didact Gothic", "Century Gothic", sans-serif;
  }
  .letterhead {
    position: absolute;
    left: 289px;
    top: 63px;
    width: 623px;
    height: 879px;
    background: var(--paper);
    overflow: hidden;
  }
  .letterhead-header {
    position: absolute;
    left: 0; top: 0;
    width: 100%;
    height: 84px;
    background: var(--plum);
    border-bottom: 4px solid var(--gold);
  }
  .brand-name {
    position: absolute;
    left: 58px;
    top: 19px;
    color: var(--gold);
    font-size: 34px;
    line-height: 40px;
    letter-spacing: 2px;
    white-space: nowrap;
  }
  .sender-address {
    position: absolute;
    right: 57px;
    top: 27px;
    text-align: right;
    color: var(--white);
    font-size: 8.5px;
    line-height: 11px;
    font-style: normal;
  }
  .letter-body {
    position: absolute;
    left: 58px;
    top: 291px;
    width: 508px;
    color: var(--ink);
    font-size: 9.6px;
    line-height: 11.7px;
    letter-spacing: 0.15px;
  }
  .salutation {
    font-weight: bold;
    margin: 0 0 11px;
  }
  .letter-body p {
    margin: 0 0 9px;
    text-align: justify;
  }
  .sign-off {
    position: absolute;
    left: 58px;
    top: 563px;
    font-size: 9.2px;
    line-height: 11px;
    color: var(--ink);
  }
  .sign-off strong { display: block; }
  .signature {
    position: absolute;
    left: 132px;
    top: 555px;
    width: 130px;
    height: 62px;
    background: linear-gradient(135deg, rgba(90,110,190,0.18), rgba(90,110,190,0.05));
  }
  .contact-line {
    position: absolute;
    left: 58px;
    top: 840px;
    font-size: 8.5px;
    color: var(--ink);
  }
  .contact-line b { color: var(--plum); }
  .website {
    position: absolute;
    right: 57px;
    top: 840px;
    font-size: 8.5px;
    color: var(--ink);
  }
  .website b { color: var(--plum); }
  .footer-band {
    position: absolute;
    left: 0;
    bottom: 0;
    width: 623px;
    height: 14px;
  }
</style>
</head>
<body>
  <main class="letterhead">
    <header class="letterhead-header">
      <div class="brand-name">KA VERLINE</div>
      <address class="sender-address">
        18 Harbour Crest Road<br>
        Singapore 439021
      </address>
    </header>

    <section class="letter-body">
      <p class="salutation">Dear sir,</p>
      <p>Communication is a very integral part of living creatures, animals and humans. Communication may be verbal or written. Written communication however is only applicable to human beings. Can you even imagine a world without communication? Verbal communication can be through telephones, webcams or in person. Written communication is through letters, emails and mobile phone messages.</p>
      <p>In today’s world of great inventions and technology, letters have somehow become redundant. It is the time for text messages or chats. But they still can communicate a lot more than all other modes of communication. Organizations and various government departments still bank on letters as a strong medium of communication. There is no comparison in costs of sending letters as compared to costs of mobile phone messages though – letters are far cheaper. Letters now commonly known as “hard copy documents” are considered more relevant and important than email copies of text messages as proof or evidence of some sort.</p>
      <p>Letters speak volumes about a person or an organization that writes it. So one must take utmost care ensuring that the language used in any letter is appropriate for the occasion for which it is being written. Since a letter is also a written proof or document, if there are certain things that should not form a part of it, then that too should be carefully handled.</p>
      <p>Writing a good letter is an art. But if for some reason someone is unable to write that perfect letter, these different types of letters provide a base for you to build on. Sample letters have been given for everyone to understand what all information needs to form a part of the letter type and then it can be customized.</p>
    </section>

    <div class="sign-off">
      Yours Sincerely,
      <strong>Lera Doman</strong>
    </div>
    <div class="signature" role="img" aria-label="Handwritten signature in blue ink"></div>

    <div class="contact-line">
      <b>Tel:</b> +65-6000 4120 · <b>Fax:</b> +65-6000 4121 · <b>Email:</b> info@kaverline.com
    </div>
    <div class="website">www.<b>kaverline</b>.com</div>

    <svg class="footer-band" viewBox="0 0 623 14" aria-hidden="true">
      <defs>
        <linearGradient id="footerGold" x1="0" y1="0" x2="1" y2="0">
          <stop offset="0" stop-color="#b8860b"/>
          <stop offset="0.6" stop-color="#d9a514"/>
          <stop offset="1" stop-color="#f0c52e"/>
        </linearGradient>
      </defs>
      <rect x="0" y="0" width="623" height="14" fill="#3d2549"/>
      <polygon points="410,0 623,0 623,14 424,14" fill="url(#footerGold)"/>
    </svg>
  </main>
</body>
</html>
```